Detox Poster Design Project

I am a naturopath that works in Melbourne. I require a poster that I can put up in my natural therapies clinic that is advertising a detox program that I am offering. The program runs for 3 or 6 weeks and is designed to help your liver, gut and kidney cleanse toxins more efficiently, leaving you feeling energised and healthy.

I would like to see designs that are fresh, organic, clear and contemporary to look at. I want to sell the idea of feeling good, wellbeing and vitality to the potential client. Colours I like include greens, greys and blues.

The final design should communicate health and happiness.

Requirements
Must have
• Please include the photo of the woman in nature.Poster size will be A2 594mm by 420mm
Nice to have
• I have attached the design work for my business cards that you can use. It would be great if the colours and style are in keeping with the existing design work for my business. I have also attached an extra image (almond milk photo) just in case you could see a use for it.

Many thanks.
Should not have
• No hippy, new age looking design.

```html
<!DOCTYPE html>
<html lang="en">
<head>
<meta charset="utf-8">
<title>Sensible Detox Time</title>
<link href="https://fonts.googleapis.com/css2?family=Bebas+Neue&display=swap" rel="stylesheet">
<style>
  :root {
    --leaf-green: #5b8c52;
    --sky-blue: #2a9ad6;
    --paper: #ffffff;
    --forest-dark: #3f6b33;
    --forest-mid: #7fa85a;
    --forest-light: #c9dca4;
    --sun-haze: #eef3dc;
  }
  html, body {
    margin: 0;
    padding: 0;
    overflow: hidden;
    background: var(--paper);
  }
  .poster {
    position: relative;
    width: 849px;
    height: 1200px;
    overflow: hidden;
    background: var(--paper);
    font-family: "Bebas Neue", "Oswald", sans-serif;
  }
  .hero-photo {
    position: absolute;
    left: 0;
    top: 0;
    width: 849px;
    height: 900px;
    background:
      radial-gradient(ellipse at 78% 12%, var(--sun-haze) 0%, rgba(238,243,220,0) 38%),
      radial-gradient(ellipse at 50% 55%, #e9dccb 0%, rgba(233,220,203,0) 22%),
      linear-gradient(to bottom, var(--forest-mid) 0%, var(--forest-dark) 30%, #6f9a4e 55%, var(--forest-light) 72%, var(--paper) 96%);
  }
  .headline {
    position: absolute;
    left: 53px;
    top: 696px;
    margin: 0;
    font-weight: 400;
    font-size: 130px;
    line-height: 116px;
    letter-spacing: 1px;
    color: var(--leaf-green);
    text-transform: uppercase;
  }
  .pitch {
    position: absolute;
    left: 55px;
    top: 920px;
    margin: 0;
    padding: 0;
    list-style: none;
    font-size: 27px;
    line-height: 45.5px;
    letter-spacing: 0.6px;
    color: var(--sky-blue);
    text-transform: uppercase;
  }
  .contact {
    position: absolute;
    right: 48px;
    top: 1104px;
    margin: 0;
    text-align: right;
    font-size: 25px;
    line-height: 35px;
    letter-spacing: 0.6px;
    color: var(--leaf-green);
    text-transform: uppercase;
  }
</style>
</head>
<body>
  <main class="poster">
    <div class="hero-photo" role="img" aria-label="Photo of a woman seen from behind with arms raised, standing in lush green tropical foliage in soft sunlight"></div>

    <h1 class="headline">It’s sensible<br>detox time</h1>

    <ul class="pitch">
      <li>Overindulge over the holidays?</li>
      <li>Have a detox program tailored for you.</li>
      <li>Press reset on your bad eating habits to feel energised and vital.</li>
    </ul>

    <p class="contact">
      For more information, contact Clara Whitfield on 0400 218 637<br>
      or email: info@thegreenleafnaturopath.com
    </p>
  </main>
</body>
</html>
```